Harbour Press website re-design

We would like to recreate the www.harbourpress.example.au website into a simpler and more sophisticated version. We want the buyer to be drawn to our site and establish that we are reputable and professional from the moment they enter. We want them to easily find the product or service they are looking for within our site, decide that they would like to find out more and either click through to obtain a quote or click through to contact a rep.

The current website has been created using MS Front Page, however we would like the newly designed site to be created in a mobile responsive WordPress CMS format

We are a Print Broker who can save clients time in hunting around for the right supplier for their print jobs. This is most likely appealing to larger organisations who haven’t got time to waste in finding quotes from many different suppliers for each type of job. We make it easy because we have access to a large network of trade only print & signage suppliers so we can select the best and most cost effective supplier depending on the type of print job. Further, because we don’t do the printing in-house we have low overheads which means we can ensure competitive prices.
Updates

Target Market(s)

Business owners, print managers, receptionists, marketing managers who are time poor, uneducated re:printing, after quick & cost effective solutions

Industry/Entity Type

Printing

Requirements
Must have
• Use the current logo and colours - see files uploaded
Limit scrolling and keep pages within view
Easy to see buttons that navigate the buyer through the site
The site is to be clear, easy to understand, free from clutter (ie.ensure white space) and have a Professional/corporate look
Easy to use Quotation forms
Imagery needs to be modern, and clean -see duskmarble site

Competitor/other websites we like and why?
I like duskmarble.example.au for its’ modern look. I like how the products are displayed in High resolution are very clean and uncluttered. You can easily find the product and access ‘get a quote’.
Calloway Print has a good layout for the quote request. Check out callowayprint.example.au
www.vendrelo.example.au are print brokers/managers. Their descriptions are easy to understand but still heavy in content.
Nice to have
• 1. Home Page
½ page summary of the core business
Distinct buttons for products and services down the side (so that people can go straight to what they need.)
About Us (including profiles); Products and Services; Get a Quote; Contact us across the top

2. About Us
A brief overview of owner, staff and reps. Click through to Profiles for each region rep and contact details either as pop ups or separate pages.

3. Products and Services
Buttons or lists of products link to pop up with get a quote link within (this could be grouped such as Business Cards, Letterheads, Folders etc.; Club printing with plastic cards, sign in books, coasters etc.; Marketing such as flyers, posters, banners etc. (Note. look at how others have broken it up)
Include calling for advice for special products and finishes as service on how a job can be improved and done within budget.
4. Get a Quote
(2 sites mentioned below that I like for the get a quote system)

5. Contact Us
Clear sections divided by lines and details large starting with 1300 number
Head office
Regional numbers and areas they cover
Include emails.

Contact us now or click to request a rep contact you.

```html
<!DOCTYPE html>
<html lang="en">
<head>
<meta charset="utf-8">
<title>Harbour Press – Commercial Printing &amp; Signage</title>
<link rel="stylesheet" href="https://fonts.googleapis.com/css2?family=Maven+Pro:wght@500;600;700;800&family=Open+Sans:wght@400;600;700&display=swap">
<style>
:root{
  --brand-red:#a8192e;
  --brand-red-dark:#7d0f1f;
  --footer-red:#b5162b;
  --ink:#111;
  --body-text:#555;
  --hero-pink:#e7b9c0;
  --white:#fff;
  --rule:#dcdcdc;
  --screen-dark:#1c1c1c;
}
*{box-sizing:border-box;margin:0;padding:0}
html,body{width:1200px;height:1138px;overflow:hidden;background:var(--white)}
body{position:relative;font-family:"Open Sans",Arial,sans-serif;color:var(--ink)}
.hero{position:absolute;left:0;top:0;width:1200px;height:737px;
  background:linear-gradient(180deg,#f3dde1 0%,var(--hero-pink) 30%,#efd0d5 55%,var(--white) 100%);
  border-bottom:1px solid var(--rule)}
.hero::before{content:"";position:absolute;inset:0;
  background:radial-gradient(ellipse at 85% 10%,rgba(200,110,125,.35),transparent 55%),
             radial-gradient(ellipse at 10% 20%,rgba(255,255,255,.45),transparent 50%)}
.call-tab{position:absolute;left:802px;top:0;width:225px;height:36px;background:#000;
  border-radius:0 0 8px 8px;color:var(--white);font-family:"Maven Pro",sans-serif;font-weight:700;
  font-size:14px;display:flex;align-items:center;justify-content:center}
.brand{position:absolute;left:173px;top:40px;display:flex;align-items:center;gap:10px}
.brand-mark{width:34px;height:34px;background:var(--brand-red);border-radius:6px}
.brand-name{font-family:"Maven Pro",sans-serif;font-weight:700;font-size:25px;color:var(--brand-red)}
.main-nav{position:absolute;right:173px;top:74px;display:flex;align-items:center;gap:6px}
.main-nav a{font-family:"Maven Pro",sans-serif;font-weight:600;font-size:16.5px;color:var(--ink);
  text-decoration:none;padding:4px 13px;border-radius:6px}
.main-nav a:last-child{padding-right:0}
.main-nav a.is-active{background:var(--brand-red);color:var(--white)}
.hero-title{position:absolute;left:0;width:1200px;top:141px;text-align:center;
  font-family:"Maven Pro",sans-serif;font-weight:800;font-size:30px;letter-spacing:-.3px;color:var(--ink)}
.hero-sub{position:absolute;left:0;width:1200px;top:183px;text-align:center;font-size:13.5px;color:#222}
.showcase{position:absolute;left:348px;top:242px;width:498px;height:385px;border-radius:24px;
  background:linear-gradient(160deg,#3a3a3a 0%,var(--screen-dark) 45%,#0e0e0e 100%)}
.slide-caption{position:absolute;left:396px;top:552px;width:403px;height:34px;background:rgba(60,60,60,.85);
  color:var(--white);font-size:13.5px;display:flex;justify-content:space-between;align-items:center;padding:0 14px 0 16px}
.slide-arrow{position:absolute;top:408px;width:44px;height:44px}
.slide-arrow.prev{left:207px}
.slide-arrow.next{left:950px}
.cta-quote{position:absolute;left:491px;top:638px;width:219px;height:54px;background:var(--brand-red);
  border-bottom:4px solid var(--brand-red-dark);border-radius:6px;color:var(--white);
  font-size:16.5px;display:flex;align-items:center;justify-content:center}
.welcome{position:absolute;left:173px;top:806px;width:562px}
.welcome h1{font-family:"Maven Pro",sans-serif;font-weight:700;font-size:29px;line-height:29px;color:var(--ink)}
.welcome p{margin-top:11px;font-size:12.5px;line-height:20px;color:var(--body-text)}
.welcome p a{color:var(--brand-red);text-decoration:none}
.call-card{position:absolute;left:772px;top:802px;width:254px;height:222px;border:1px solid var(--rule);
  background:var(--white);box-shadow:0 1px 3px rgba(0,0,0,.08)}
.call-card .agent-photo{position:absolute;left:8px;top:8px;width:163px;height:204px;
  background:linear-gradient(135deg,#f1dccf 0%,#e8c6b2 50%,#f7f2ee 100%)}
.call-card .call-text{position:absolute;right:18px;top:148px;text-align:right;font-size:12px;line-height:17px;color:#333}
.call-card .call-number{display:block;margin-top:2px;font-weight:700;font-size:20px;color:var(--brand-red-dark)}
.site-footer{position:absolute;left:0;top:1070px;width:1200px;height:68px;background:var(--footer-red);color:var(--white)}
.footer-nav{position:absolute;left:173px;top:18px;display:flex;gap:20px;font-size:12px}
.footer-nav a{color:var(--white);text-decoration:none}
.copyright{position:absolute;left:174px;top:35px;font-size:12px}
.social{position:absolute;right:173px;top:20px;display:flex;gap:16px}
.social span{width:26px;height:26px;border-radius:50%;background:var(--white)}
</style>
</head>
<body>
<header class="hero">
  <div class="call-tab">Call Us : +61 2 5550 0147</div>
  <div class="brand"><span class="brand-mark"></span><span class="brand-name">Harbour Press</span></div>
  <nav class="main-nav">
    <a href="#">Home</a>
    <a href="#" class="is-active">About Us</a>
    <a href="#">Products and Services</a>
    <a href="#">Get a Quote</a>
    <a href="#">Contact Us</a>
  </nav>
  <h2 class="hero-title">YOUR COMMERCIAL PRINTING &amp; SIGNAGE SPECIALIST</h2>
  <p class="hero-sub">Lorem ipsum dolor sit amet, consectetur adipisicing elit, sed do eiusmod tempor incididunt&nbsp; lorem ipsum</p>
  <div class="showcase" role="img" aria-label="Hands holding a tablet showing colourful hexagonal printed brochure cards"></div>
  <div class="slide-caption"><span>Brochure Design</span><span>Learn More</span></div>
  <svg class="slide-arrow prev" viewBox="0 0 44 44" aria-label="Previous slide"><circle cx="22" cy="22" r="22" fill="#fff" opacity=".55"/><path d="M25 13 L16 22 L25 31" fill="none" stroke="#c8b8bb" stroke-width="5" stroke-linecap="round" stroke-linejoin="round"/></svg>
  <svg class="slide-arrow next" viewBox="0 0 44 44" aria-label="Next slide"><circle cx="22" cy="22" r="22" fill="#fff" opacity=".55"/><path d="M19 13 L28 22 L19 31" fill="none" stroke="#c8b8bb" stroke-width="5" stroke-linecap="round" stroke-linejoin="round"/></svg>
  <a class="cta-quote">GET A FREE QUOTE</a>
</header>

<section class="welcome">
  <h1>Welcome to Harbour Press your graphic design arisbane branding agency</h1>
  <p>Lorem ipsum dolor sit amet, consectetur adipisicing elit, sed do eiusmod tempor incididunt ut labore et dolore magna aliqua. Ut enim ad minim veniam, quis nostrud exercitation ullamco laboris nisi ut aliquip ex ea commodo consequat. Duis aute irure dolor in reprehenderit in voluptate velit esse cillum dolore eu fugiat nulla pariatur. Excepteur sint occaecat cupidatat non proident, sunt in culpa qui officia deserunt mollit anim id est laborum. Sed ut perspiciatis unde omnis iste natus error sit voluptatem accusantium doloremque laudantium, totam rem aperiam, eaque ipsa quae ab illo inventore veritatis et quasi architecto beatae vitae dicta sunt - <a href="#">Read More</a></p>
</section>

<aside class="call-card">
  <div class="agent-photo" role="img" aria-label="Customer service representative wearing a headset"></div>
  <p class="call-text">CALL US FOR A<br>PRINTING QUOTE ON<span class="call-number">1300 555 018</span></p>
</aside>

<footer class="site-footer">
  <nav class="footer-nav">
    <a href="#">Home</a><a href="#">About Us</a><a href="#">Products and Services</a><a href="#">Get a Quote</a><a href="#">Contact Us</a>
  </nav>
  <p class="copyright">All Right Resrved © 2013 &nbsp; - &nbsp;Designed by brightlanestudio.example.com</p>
  <div class="social"><span aria-label="Social link"></span><span aria-label="Social link"></span></div>
</footer>
</body>
</html>
```